Business Card for my Photography/Video Business

I would like the card to say Event Photographer and Videographer. I like the Black and Gold look to it as well but open to other options. I don't want it to be super vibrant or colorful. Simple, elegant and professional

```html
<!DOCTYPE html>
<html lang="en">
<head>
<meta charset="utf-8">
<title>Lumen Reel — Business Card</title>
<link rel="stylesheet" href="https://fonts.googleapis.com/css2?family=Montserrat:wght@500;600&display=swap">
<style>
  :root {
    --backdrop: #1c1c1c;
    --ink: #0b0b0b;
    --gold-light: #f2d85a;
    --gold-mid: #e2b52e;
    --gold-deep: #b98a14;
    --gold-text: #d9aa2a;
  }
  * { margin: 0; padding: 0; box-sizing: border-box; }
  html, body {
    width: 1200px; height: 997px; overflow: hidden;
    background: var(--backdrop);
    font-family: "Montserrat", sans-serif;
  }
  .stage {
    width: 1200px; height: 997px;
    display: flex; align-items: center; justify-content: center; gap: 40px;
  }
  .card {
    width: 540px; height: 310px;
    border-radius: 22px;
    overflow: hidden;
    background: var(--ink);
    display: flex; flex-direction: column;
  }
  .band-top { height: 44px; background: var(--ink); }
  .panel {
    flex: 1;
    background: radial-gradient(ellipse at 45% 40%, var(--gold-light) 0%, var(--gold-mid) 55%, var(--gold-deep) 100%);
    display: flex; flex-direction: column; align-items: center; justify-content: center;
  }
  .band-bottom {
    height: 72px; background: var(--ink);
    display: flex; align-items: center; justify-content: center;
  }
  .brand-name {
    font-weight: 600; font-size: 50px; letter-spacing: 4px;
    color: var(--ink); text-transform: uppercase; line-height: 1;
  }
  .tagline {
    font-weight: 500; font-size: 22px; color: var(--gold-text); letter-spacing: 0.5px;
  }
  .card-back .band-bottom { height: 60px; }
  .card-back .brand-name { font-size: 44px; }
  .contacts {
    margin-top: 22px;
    display: flex; flex-direction: column; align-items: center; gap: 6px;
    font-size: 13px; font-weight: 500; color: var(--ink);
  }
  .contact-row { display: flex; gap: 20px; }
  .contact { display: flex; align-items: center; gap: 6px; }
  .contact svg { width: 12px; height: 12px; fill: none; stroke: var(--ink); stroke-width: 2; }
</style>
</head>
<body>
<main class="stage">
  <section class="card card-front">
    <div class="band-top"></div>
    <div class="panel">
      <span class="brand-name">Lumen Reel</span>
    </div>
    <div class="band-bottom">
      <p class="tagline">Event Photographer &amp; Videographer</p>
    </div>
  </section>

  <section class="card card-back">
    <div class="band-top"></div>
    <div class="panel">
      <span class="brand-name">Lumen Reel</span>
      <div class="contacts">
        <div class="contact-row">
          <span class="contact">
            <svg viewBox="0 0 24 24"><path d="M5 3h4l2 5-3 2a12 12 0 0 0 6 6l2-3 5 2v4a2 2 0 0 1-2 2A18 18 0 0 1 3 5a2 2 0 0 1 2-2z"/></svg>
            1300 555 019
          </span>
          <span class="contact">
            <svg viewBox="0 0 24 24"><rect x="3" y="5" width="18" height="14" rx="2"/><path d="M3 7l9 6 9-6"/></svg>
            hello@lumenreel.com
          </span>
        </div>
        <span class="contact">
          <svg viewBox="0 0 24 24"><circle cx="12" cy="12" r="9"/><path d="M3 12h18M12 3c3 3 3 15 0 18M12 3c-3 3-3 15 0 18"/></svg>
          www.lumenreel.com
        </span>
      </div>
    </div>
    <div class="band-bottom"></div>
  </section>
</main>
</body>
</html>
```